Stonegate Towing Business Card

Towing
Accident towing
Mechanical breakdown
Insurance, salvage and recovery
4wd off road towing
Light & Heavy towing
7354 2618
24 hour business 7 days

Logo can be whole size on front

Industry/Entity Type

Towing/ transport

Contact Information for Business Card

The above

```html
<!DOCTYPE html>
<html lang="en">
<head>
<meta charset="utf-8">
<title>Stonegate Towing Business Card</title>
<link href="https://fonts.googleapis.com/css2?family=Roboto:wght@400;700&family=Roboto+Condensed:wght@700&display=swap" rel="stylesheet">
<style>
  :root {
    --backdrop: #3b3b3d;
    --brand-red: #d42027;
    --ink-black: #111111;
    --paper-white: #ffffff;
  }
  * { margin: 0; padding: 0; box-sizing: border-box; }
  html, body { width: 1200px; height: 689px; overflow: hidden; background: var(--backdrop); }
  .canvas { position: relative; width: 1200px; height: 689px; font-family: "Roboto", Arial, sans-serif; }
  .card {
    position: absolute; top: 190px; width: 540px; height: 310px;
    border-radius: 18px; overflow: hidden;
  }
  .card--front { left: 40px; background: var(--brand-red); color: var(--paper-white); }
  .card--back { left: 620px; background: var(--paper-white); }

  .wordmark {
    font-family: "Roboto", Arial, sans-serif; font-weight: 700;
    text-align: center; letter-spacing: 0.5px; line-height: 1;
  }
  .card--front .wordmark {
    position: absolute; left: 0; right: 0; top: 96px;
    font-size: 46px; color: var(--paper-white);
  }
  .services {
    position: absolute; left: 0; right: 0; bottom: 40px;
    text-align: center; font-size: 14px; line-height: 1.55;
  }
  .services .dot { display: inline-block; width: 6px; height: 6px; border-radius: 50%; background: var(--paper-white); margin: 0 7px 2px; vertical-align: middle; }

  .back-waves { position: absolute; inset: 0; width: 540px; height: 310px; }
  .card--back .wordmark {
    position: absolute; left: 100px; width: 380px; top: 62px;
    font-size: 36px; color: var(--brand-red);
  }
  .contact-person {
    position: absolute; left: 60px; width: 232px; top: 226px;
    text-align: right; color: var(--paper-white);
  }
  .contact-person .name { font-family: "Roboto Condensed", Arial, sans-serif; font-weight: 700; font-size: 24px; letter-spacing: 0.5px; line-height: 1; }
  .contact-person .role { font-size: 13px; margin-top: 3px; }
  .divider { position: absolute; left: 304px; top: 200px; width: 1px; height: 66px; background: var(--paper-white); }
  .contact-list { position: absolute; left: 318px; top: 198px; list-style: none; color: var(--paper-white); font-size: 13px; line-height: 23px; }
  .contact-list li { display: flex; align-items: center; gap: 8px; }
  .contact-list svg { width: 12px; height: 12px; flex: none; }
  .hours { position: absolute; left: 258px; top: 274px; display: flex; align-items: center; gap: 8px; color: var(--paper-white); font-size: 13px; }
  .hours .badge { width: 26px; height: 26px; border: 2px solid var(--paper-white); border-radius: 50%; font-size: 8px; font-weight: 700; display: flex; align-items: center; justify-content: center; }
</style>
</head>
<body>
<main class="canvas">
  <section class="card card--front" aria-label="Business card front">
    <div class="wordmark">Stonegate Towing</div>
    <p class="services">
      Towing<span class="dot"></span>Accident towing<span class="dot"></span>Mechanical breakdown<span class="dot"></span>Light &amp; Heavy towing<br>
      Insurance, salvage &amp; recovery<span class="dot"></span>4wd off road towing
    </p>
  </section>

  <section class="card card--back" aria-label="Business card back">
    <svg class="back-waves" viewBox="0 0 540 310" aria-hidden="true">
      <path d="M0 262 C140 170 330 140 540 58 L540 100 C320 160 150 178 0 250 Z" fill="var(--ink-black)"/>
      <path d="M0 250 C150 178 320 160 540 100 L540 310 L0 310 Z" fill="var(--brand-red)"/>
    </svg>
    <div class="wordmark">Stonegate Towing</div>
    <div class="contact-person">
      <div class="name">ALEX MORGAN</div>
      <div class="role">President</div>
    </div>
    <div class="divider"></div>
    <ul class="contact-list">
      <li><svg viewBox="0 0 24 24"><path fill="#fff" d="M6.6 10.8a15 15 0 0 0 6.6 6.6l2.2-2.2a1 1 0 0 1 1-.25 11.4 11.4 0 0 0 3.6.57 1 1 0 0 1 1 1V20a1 1 0 0 1-1 1A17 17 0 0 1 3 4a1 1 0 0 1 1-1h3.5a1 1 0 0 1 1 1c0 1.25.2 2.45.57 3.57a1 1 0 0 1-.25 1z"/></svg>7354 2618</li>
      <li><svg viewBox="0 0 24 24"><path fill="#fff" d="M2 5h20v14H2z M2 5l10 8 10-8" stroke="#d42027" stroke-width="1.5"/></svg>info@stonegatetowing.com</li>
      <li><svg viewBox="0 0 24 24"><circle cx="12" cy="12" r="10" fill="#fff"/></svg>www.stonegatetowing.com</li>
    </ul>
    <div class="hours"><span class="badge">24/7</span>24 hour business 7 days</div>
  </section>
</main>
</body>
</html>
```